RFID Blocker - Business Card Design

Design a business card that will be printed onto a plastic RFID blocker wallet card, this card has a space on each side of teh card that will not be printed. One side of the card is to have the contact information, and the other to have a graphic which will symbolize blocking or shielding technology. I like the phrase "Card Guard". Many people i give this card to may not realize it is a RFID blocker, and i would liek to have small icons on each side representing what it is, see attachment. I will include a few pics found on internet i was using as ideas, and also the RFID card template which shows the area that will not be printed (within the red squares). I like the shield aspect, i was originally thinking of the tessaroo shield with my logo coming out of it like the tessaroo except the black is to dark of a color. the smiley face i use within some of my software. company name is: "norvalyx software inc." - I prefer to use small print and no capitals in my company name. company from Canada - my original business card is included in files

Target Market(s)

companies wanting to hire indigenous workers, and indigenous workers looking for employment

Contact Information for Business Card

should include logo with name, title, phone, email and website. our company specializes in first nations indigenous employment software

Font styles to use
Serif
Sans Serif

Requirements
Must have
• Logo
• Name
• Title
• Phone
• email
• website

```html
<!DOCTYPE html>
<html lang="en">
<head>
<meta charset="UTF-8">
<title>norvalyx software inc. – Business Card</title>
<link href="https://fonts.googleapis.com/css2?family=Open+Sans:wght@400;600;700&display=swap" rel="stylesheet">
<style>
  :root {
    --stage: #2b2b2d;
    --card-white: #ffffff;
    --navy-deep: #071428;
    --navy-mid: #0d2a4a;
    --navy-glow: #1d4f7a;
    --brand-blue: #1479c4;
    --text-grey: #6d6e71;
    --logo-grey: #8a8c8f;
    --logo-light: #c9ccd1;
    --divider: #8d8d8d;
  }
  * { box-sizing: border-box; margin: 0; padding: 0; }
  html, body {
    width: 1200px; height: 900px; overflow: hidden;
    background: var(--stage);
    font-family: "Open Sans", "Segoe UI", sans-serif;
  }
  .canvas {
    position: relative; width: 1200px; height: 900px;
  }
  .card {
    position: absolute; left: 290px; width: 620px; height: 350px;
    box-shadow: 0 10px 30px rgba(0,0,0,0.45);
    overflow: hidden;
  }
  /* Back side */
  .card-back { top: 55px; background: var(--navy-deep); }
  .circuit-art {
    position: absolute; inset: 0;
    background:
      radial-gradient(circle at 55% 48%, var(--navy-glow) 0%, var(--navy-mid) 35%, var(--navy-deep) 80%);
  }
  .back-logo {
    position: absolute; left: 0; right: 0; top: 50%;
    transform: translateY(-50%);
    display: flex; justify-content: center; align-items: center; gap: 14px;
  }
  .back-logo .logo-dot {
    width: 22px; height: 22px; border-radius: 50%; background: var(--brand-blue);
  }
  .back-logo .logo-name {
    font-size: 58px; font-weight: 600; color: var(--logo-light); letter-spacing: 0.5px;
  }

  /* Front side */
  .card-front { top: 475px; background: var(--card-white); }
  .front-logo {
    position: absolute; left: 52px; top: 140px;
    display: flex; align-items: center; gap: 12px;
  }
  .front-logo .logo-dot {
    width: 18px; height: 18px; border-radius: 50%; background: var(--brand-blue);
  }
  .front-logo .logo-name {
    font-size: 46px; font-weight: 600; color: var(--logo-grey);
  }
  .divider {
    position: absolute; left: 322px; top: 85px; width: 2px; height: 165px;
    background: var(--divider);
  }
  .contact {
    position: absolute; left: 348px; top: 88px;
  }
  .contact .person-name {
    font-size: 25px; font-weight: 700; color: var(--brand-blue); line-height: 1.1;
  }
  .contact .person-title {
    font-size: 18px; color: var(--text-grey); margin-bottom: 12px;
  }
  .contact ul { list-style: none; }
  .contact li {
    display: flex; align-items: center; gap: 12px;
    font-size: 18px; color: var(--text-grey); line-height: 1.45;
  }
  .contact li svg { width: 18px; height: 18px; flex: none; fill: var(--brand-blue); }
</style>
</head>
<body>
<main class="canvas">

  <section class="card card-back">
    <div class="circuit-art" role="img" aria-label="Glowing blue circuit-board pattern symbolising shielding technology"></div>
    <div class="back-logo">
      <span class="logo-dot"></span>
      <span class="logo-name">norvalyx</span>
    </div>
  </section>

  <section class="card card-front">
    <div class="front-logo">
      <span class="logo-dot"></span>
      <span class="logo-name">norvalyx</span>
    </div>
    <div class="divider"></div>
    <div class="contact">
      <p class="person-name">YOUR NAME</p>
      <p class="person-title">Your Title</p>
      <ul>
        <li>
          <svg viewBox="0 0 24 24" aria-hidden="true"><path d="M6.6 10.8a15.1 15.1 0 0 0 6.6 6.6l2.2-2.2c.3-.3.7-.4 1-.2 1.1.4 2.3.6 3.6.6.6 0 1 .4 1 1V20c0 .6-.4 1-1 1A17 17 0 0 1 3 4c0-.6.4-1 1-1h3.5c.6 0 1 .4 1 1 0 1.3.2 2.5.6 3.6.1.3 0 .7-.2 1z"/></svg>
          <span>123-456-2100</span>
        </li>
        <li>
          <svg viewBox="0 0 24 24" aria-hidden="true"><path d="M2 5h20v14H2z M4 7v.4l8 5.2 8-5.2V7z" fill-rule="evenodd"/></svg>
          <span>youremail@mailnest.com</span>
        </li>
        <li>
          <svg viewBox="0 0 24 24" aria-hidden="true"><path d="M12 2a10 10 0 1 0 0 20 10 10 0 0 0 0-20zm0 2.2c1 1.2 1.8 3 2.1 4.8H9.9c.3-1.8 1.1-3.6 2.1-4.8zM4.6 11h3.2a16 16 0 0 0 0 2H4.6a7.6 7.6 0 0 1 0-2zm5.2 0h4.4a14 14 0 0 1 0 2H9.8a14 14 0 0 1 0-2zm6.4 0h3.2a7.6 7.6 0 0 1 0 2h-3.2a16 16 0 0 0 0-2zM9.9 15h4.2c-.3 1.8-1.1 3.6-2.1 4.8-1-1.2-1.8-3-2.1-4.8z"/></svg>
          <span>www.yourwebsite.com</span>
        </li>
      </ul>
    </div>
  </section>

</main>
</body>
</html>
```